Design profile for MuroDeck Nordhaven

I had a logo competition here recently, and was left with two logos that I could not choose between. Therefore, I create this competition where I want a complete design package or a visual identity for the company. I want you to create design elements that can be used both in print and online. (letterhead, envelopes, business card, website, facebook, etc.) I have also attached a picture of the car I have ordered. I'm happy if you can show how the design can be used on that as well.
What is important is that the logos are treated individually, and that the design you create reflects or builds up under the logo. I want the design to be recognizable and to have a connection with the logo and what we do. (take fizzo lumo as an example. if you remove the name, but keep the red color and the white line, then you will recognize which brand it is about right away)
You choose whether you want to make proposals only for one logo, or or both, but it is important that they are treated individually. The best overall package determines which logo I use.
I have also added an image that you can use as an example background if you want it in a facebook banner for example.
It is important that the design looks professional and unique. A number of designs have come in, but many of the designs are very similar and general. Here is a video of the printer if you need inspiration: https://clipvault.example/v/Q8ZtrMx2LwK

Industry/Entity Type

WallPrinting

Requirements
Must have
• Unique an professional design that can be used both online and print
Nice to have
• Show how to use the design on a VX Tully. (see photos attached)
Should not have
• The design can be simple, but not too simple and general. I want it to give the company an identity

```html
<!DOCTYPE html>
<html lang="en">
<head>
<meta charset="utf-8">
<title>MuroDeck Nordhaven – Stationery Set</title>
<link href="https://fonts.googleapis.com/css2?family=Ubuntu:wght@400;500;700&display=swap" rel="stylesheet">
<style>
  :root{
    --stage:#87888c;
    --ink:#050304;
    --paper:#ffffff;
    --blue-deep:#0053a6;
    --blue-mid:#0a7fd0;
    --blue-bright:#00aeef;
    --yellow:#ffd400;
    --pink:#ec008c;
    --text-light:#ffffff;
    --icon:#c21d8a;
    --stripe-warm:linear-gradient(to bottom,#ffd400 0 12.5%,#f7941d 12.5% 25%,#f26522 25% 37.5%,#c1272d 37.5% 50%,#7a1018 50% 62.5%,#4a0c12 62.5% 75%,#2a0a0e 75% 87.5%,#0a0a0a 87.5% 100%);
    --stripe-cool:linear-gradient(to bottom,#f49ac1 0 12.5%,#ec008c 12.5% 25%,#92278f 25% 37.5%,#662d91 37.5% 50%,#44206b 50% 62.5%,#2e1248 62.5% 75%,#1a1025 75% 87.5%,#0a0a0a 87.5% 100%);
    --stripe-cool-up:linear-gradient(to top,#ffffff 0 6%,#f49ac1 6% 18%,#ec008c 18% 30%,#92278f 30% 42%,#662d91 42% 54%,#44206b 54% 66%,#2e1248 66% 78%,#1a1025 78% 100%);
    --stripe-warm-up:linear-gradient(to top,#ffffff 0 6%,#ffd400 6% 18%,#f7941d 18% 30%,#f26522 30% 42%,#c1272d 42% 54%,#7a1018 54% 66%,#4a0c12 66% 78%,#2a0a0e 78% 100%);
    --metal-blue:linear-gradient(90deg,#0053a6 0%,#00aeef 22%,#0a6fc0 45%,#00aeef 70%,#0053a6 100%);
  }
  *{box-sizing:border-box;margin:0;padding:0}
  html,body{width:1200px;height:1200px;overflow:hidden}
  body{background:var(--stage);font-family:"Ubuntu",sans-serif;position:relative}
  .piece{position:absolute;box-shadow:0 1px 4px rgba(0,0,0,.35)}
  .piece svg{position:absolute;display:block}

  .brand-name{color:var(--text-light);font-weight:700;font-family:"Ubuntu",sans-serif;line-height:1}
  .brand-name .word{display:block;letter-spacing:-.5px}
  .brand-name .region{display:block;letter-spacing:.42em;margin-top:3px}

  .stripe{position:absolute}
  .stripe.warm{background:var(--stripe-warm)}
  .stripe.cool{background:var(--stripe-cool)}
  .stripe.warm-up{background:var(--stripe-warm-up)}
  .stripe.cool-up{background:var(--stripe-cool-up)}

  .contact{position:absolute;color:var(--text-light);font-weight:500}
  .contact li{list-style:none;display:flex;align-items:center;gap:4px;white-space:nowrap}
  .contact svg{position:static;flex:none}

  /* business card front */
  .card-front{left:114px;top:71px;width:331px;height:189px;background:var(--ink)}
  .card-front .brand-name{position:absolute;left:14px;top:52px}
  .card-front .brand-name .word{font-size:25px}
  .card-front .brand-name .region{font-size:7px}
  .card-front .holder{position:absolute;left:16px;top:154px;color:var(--text-light)}
  .card-front .holder .role{font-size:7px;font-weight:500}
  .card-front .holder .person{font-size:10px;font-weight:700;margin-top:2px}
  .card-front .contact{font-size:7px;line-height:12px}
  .card-front .contact.lines{left:106px;top:147px}
  .card-front .contact.address{left:208px;top:161px}

  /* vehicle panel */
  .vehicle-panel{left:555px;top:56px;width:498px;height:218px;background:var(--paper)}
  .vehicle-art{position:absolute;left:26px;top:16px;width:452px;height:186px;border-radius:40px 60px 24px 24px;
    background:linear-gradient(to bottom,#eef0f2 0 14%,#1c2530 14% 42%,#2c6ea6 42% 80%,#1b2f4e 80% 100%)}

  /* business card back */
  .card-back{left:114px;top:301px;width:331px;height:189px;background:var(--ink);z-index:4}
  .card-back .stripe{top:10px;width:8px;height:179px}
  .card-back .brand-name{position:absolute;right:14px;top:104px;text-align:right}
  .card-back .brand-name .word{font-size:29px}
  .card-back .brand-name .region{font-size:8px;margin-right:-.42em}
  .card-back .divider{position:absolute;right:14px;top:155px;width:130px;height:1px;background:#5a5a5a}
  .card-back .web{position:absolute;right:14px;top:164px;font-size:8px;font-weight:700;letter-spacing:.14em;color:var(--text-light)}
  .card-back .web em{font-style:normal;color:var(--yellow)}

  /* envelope front */
  .envelope-front{left:79px;top:391px;width:619px;height:269px;background:var(--paper);z-index:3;overflow:hidden}
  .envelope-front .stripe{top:14px;width:9px;height:180px}
  .envelope-front .brand-name{position:absolute;left:9px;top:227px}
  .envelope-front .brand-name .word{font-size:19px}
  .envelope-front .brand-name .region{font-size:5px}
  .envelope-front .contact{left:138px;top:219px;font-size:5.5px;line-height:7px}

  /* envelope back */
  .envelope-back{left:168px;top:692px;width:619px;height:270px;background:var(--paper);z-index:3}
  .envelope-back .flap{position:absolute;left:0;top:0;width:619px;height:87px;border-radius:0 0 26px 26px;
    background:linear-gradient(90deg,#0053a6 0%,#0a8ad6 30%,#00aeef 50%,#0a8ad6 70%,#0053a6 100%)}

  /* letterhead */
  .letterhead{left:485px;top:320px;width:637px;height:824px;background:var(--paper);z-index:1;overflow:hidden}
  .letterhead .stripe{top:18px;width:10px;height:688px}
  .letterhead .brand-name{position:absolute;left:22px;top:758px}
  .letterhead .brand-name .word{font-size:32px}
  .letterhead .brand-name .region{font-size:9px}
  .letterhead .contact{font-size:9.5px;line-height:14px}
  .letterhead .contact.lines{left:253px;top:761px}
  .letterhead .contact.address{left:388px;top:777px}
</style>
</head>
<body>

<svg width="0" height="0" style="position:absolute">
  <defs>
    <linearGradient id="arcBlue" x1="0" x2="1" y1="0" y2="0">
      <stop offset="0" stop-color="#0053a6"/><stop offset=".5" stop-color="#00aeef"/><stop offset="1" stop-color="#0a6fc0"/>
    </linearGradient>
    <linearGradient id="metalBlue" x1="0" x2="1" y1="0" y2="0">
      <stop offset="0" stop-color="#0053a6"/><stop offset=".22" stop-color="#00aeef"/><stop offset=".45" stop-color="#0a6fc0"/><stop offset=".7" stop-color="#00aeef"/><stop offset="1" stop-color="#0053a6"/>
    </linearGradient>
    <symbol id="icon-phone" viewBox="0 0 10 10"><path d="M2 1l2 2-1 1.2c.6 1.2 1.6 2.2 2.8 2.8L7 6l2 2-1.2 1.2C4.5 9 1 5.5.8 2.2z" fill="#c21d8a"/></symbol>
    <symbol id="icon-mail" viewBox="0 0 10 10"><rect x="1" y="2.5" width="8" height="5.5" rx=".6" fill="#c21d8a"/><path d="M1.3 3l3.7 2.6L8.7 3" stroke="#fff" stroke-width=".7" fill="none"/></symbol>
    <symbol id="icon-web" viewBox="0 0 10 10"><circle cx="5" cy="5" r="3.8" fill="none" stroke="#c21d8a" stroke-width="1.1"/><path d="M1.2 5h7.6M5 1.2c-2 2.4-2 5.2 0 7.6M5 1.2c2 2.4 2 5.2 0 7.6" stroke="#c21d8a" stroke-width=".7" fill="none"/></symbol>
    <symbol id="icon-pin" viewBox="0 0 10 10"><path d="M5 .8a3 3 0 0 1 3 3c0 2.2-3 5.6-3 5.6S2 6 2 3.8a3 3 0 0 1 3-3z" fill="#c21d8a"/><circle cx="5" cy="3.8" r="1.1" fill="#050304"/></symbol>
  </defs>
</svg>

<!-- Business card front -->
<section class="piece card-front" aria-label="Business card front">
  <div class="brand-name"><span class="word">MuroDeck</span><span class="region">NORDHAVEN</span></div>
  <svg width="331" height="189" viewBox="0 0 331 189" style="left:0;top:0">
    <path d="M0 117 C40 103 70 110 90 140 C100 160 110 180 118 189 L0 189Z" fill="url(#metalBlue)"/>
    <path d="M0 122 C38 110 66 116 84 144 C96 164 104 180 110 189 L0 189Z" fill="url(#metalBlue)" opacity=".85"/>
    <rect x="100" y="134" width="231" height="4" fill="#00aeef"/>
    <path d="M96 138 L331 138 L331 189 L130 189 C120 175 110 155 96 138Z" fill="url(#metalBlue)"/>
    <path d="M84 140 C96 158 108 178 116 189 L130 189 C120 175 108 155 96 138Z" fill="#050304"/>
  </svg>
  <div class="holder"><div class="role">Director</div><div class="person">ERIK LUNDVALL</div></div>
  <ul class="contact lines">
    <li><svg width="6" height="6"><use href="#icon-phone"/></svg>555-014-227</li>
    <li><svg width="6" height="6"><use href="#icon-mail"/></svg>erik@murodeck.example</li>
    <li><svg width="6" height="6"><use href="#icon-web"/></svg>www.murodeck.example</li>
  </ul>
  <ul class="contact address">
    <li><svg width="6" height="6"><use href="#icon-pin"/></svg>P.O Box 4120 Kaiveien</li>
    <li style="padding-left:10px">Harbour Row Nordby, 4120</li>
  </ul>
</section>

<!-- Vehicle application -->
<section class="piece vehicle-panel" aria-label="Vehicle livery">
  <div class="vehicle-art" role="img" aria-label="VX Tully van wrapped in blue with a white roof, dark windows and the MuroDeck Nordhaven name on the rear side window"></div>
</section>

<!-- Letterhead -->
<section class="piece letterhead" aria-label="Letterhead">
  <div class="stripe warm" style="left:586px"></div>
  <div class="stripe cool" style="left:605px"></div>
  <svg width="637" height="160" viewBox="0 0 637 160" style="left:0;top:664px">
    <rect x="150" y="50" width="487" height="110" fill="#050304"/>
    <rect x="157" y="43" width="480" height="7" fill="url(#arcBlue)"/>
    <path d="M0 22 C50 0 120 2 170 42 C210 76 236 130 260 160 L0 160Z" fill="url(#arcBlue)"/>
    <path d="M0 30 C48 10 114 12 160 50 C198 84 222 134 244 160 L0 160Z" fill="#ffffff"/>
    <path d="M0 33 C46 14 110 16 154 54 C190 86 214 134 236 160 L0 160Z" fill="#050304"/>
  </svg>
  <div class="brand-name"><span class="word">MuroDeck</span><span class="region">NORDHAVEN</span></div>
  <ul class="contact lines">
    <li><svg width="8" height="8"><use href="#icon-phone"/></svg>555-014-227</li>
    <li><svg width="8" height="8"><use href="#icon-mail"/></svg>erik@murodeck.example</li>
    <li><svg width="8" height="8"><use href="#icon-web"/></svg>www.murodeck.example</li>
  </ul>
  <ul class="contact address">
    <li><svg width="8" height="8"><use href="#icon-pin"/></svg>P.O Box 4120 Kaiveien</li>
    <li style="padding-left:12px">Harbour Row Nordby, 4120</li>
  </ul>
</section>

<!-- Envelope front -->
<section class="piece envelope-front" aria-label="Envelope front">
  <div class="stripe warm" style="left:575px"></div>
  <div class="stripe cool" style="left:591px"></div>
  <svg width="619" height="95" viewBox="0 0 619 95" style="left:0;top:174px">
    <rect x="110" y="24" width="509" height="71" fill="#050304"/>
    <rect x="102" y="20" width="517" height="4" fill="url(#arcBlue)"/>
    <path d="M0 10 C36 -4 84 0 118 30 C146 56 164 80 180 95 L0 95Z" fill="url(#arcBlue)"/>
    <path d="M0 15 C34 3 78 6 110 34 C136 58 152 82 168 95 L0 95Z" fill="#ffffff"/>
    <path d="M0 17 C32 6 74 9 104 37 C128 60 144 82 160 95 L0 95Z" fill="#050304"/>
  </svg>
  <div class="brand-name"><span class="word">MuroDeck</span><span class="region">NORDHAVEN</span></div>
  <ul class="contact">
    <li><svg width="5" height="5"><use href="#icon-pin"/></svg>P.O Box 4120 Kaiveien</li>
    <li style="padding-left:8px">Harbour Row Nordby, 4120</li>
  </ul>
</section>

<!-- Business card back -->
<section class="piece card-back" aria-label="Business card back">
  <div class="stripe cool-up" style="left:10px"></div>
  <div class="stripe warm-up" style="left:24px"></div>
  <div class="brand-name"><span class="word">MuroDeck</span><span class="region">NORDHAVEN</span></div>
  <div class="divider"></div>
  <div class="web">www.<em>murodeck</em>.example</div>
</section>

<!-- Envelope back -->
<section class="piece envelope-back" aria-label="Envelope back">
  <div class="flap"></div>
</section>

</body>
</html>
```